bramblecrest paving card makeover

were a excavation/paving contractor from Monterey ca, I'm looking to have a card designed front and back that has company details on the front and a list of the services we offer on the back.

Target Market(s)

home owners property management companies

Industry/Entity Type

Contractor

Contact Information for Business Card

bramblecrest paving 418 larkmoor st Monterey ca. licensed, insured and bonded
lic#657920 gerald pinsky operations manager

Font styles to use
Serif
Sans Serif

Colors
f78f20

Requirements
Must have
• a list of my services on back, asphalt construction and maintenance, drainage, foundations, retaining walls, chip seals, excavation, grading, landscape ground work, interlocking paver, hydro-seeding, structured and driveway demolition, utility trenching and stump removal.
Nice to have
• my new domain and page address I'm acquiring from pixel bazaar.

```html
<!DOCTYPE html>
<html lang="en">
<head>
<meta charset="utf-8">
<title>Bramblecrest Paving – Business Card</title>
<link href="https://fonts.googleapis.com/css2?family=Open+Sans:wght@400;600;700&display=swap" rel="stylesheet">
<style>
  :root {
    --canvas-bg: #1d1d1f;
    --card-bg: #050505;
    --ink: #f2f2f2;
    --ink-soft: #d8d8d8;
    --accent: #f78f20;
  }
  * { box-sizing: border-box; margin: 0; padding: 0; }
  html, body {
    width: 1200px; height: 900px; overflow: hidden;
    background: var(--canvas-bg);
    font-family: "Open Sans", Arial, sans-serif;
    color: var(--ink);
  }
  .canvas {
    width: 1200px; height: 900px;
    display: flex; flex-direction: column; align-items: center;
    justify-content: center; gap: 34px;
  }
  .card {
    width: 720px; height: 400px;
    background: var(--card-bg);
    display: flex; flex-direction: column; align-items: center;
    box-shadow: 0 6px 18px rgba(0,0,0,0.55);
  }
  .brand {
    display: flex; align-items: center; gap: 12px;
    font-weight: 600; font-size: 24px; letter-spacing: 0.5px;
    color: var(--ink);
  }
  .brand-dot {
    width: 28px; height: 28px; border-radius: 50%;
    border: 3px solid var(--accent);
  }
  /* back: services */
  .card--services { justify-content: center; gap: 44px; }
  .services {
    text-align: center; white-space: nowrap;
    font-size: 16px; line-height: 1.35; color: var(--ink-soft);
  }
  /* front: contact */
  .card--contact { padding-top: 70px; }
  .card--contact .brand { margin-bottom: 66px; }
  .person-name { font-weight: 700; font-size: 24px; }
  .person-role { font-size: 16px; color: var(--ink-soft); margin-top: 2px; }
  .address { font-size: 17px; margin-top: 20px; }
  .contact-line {
    display: flex; align-items: center; gap: 8px;
    font-size: 17px; margin-top: 6px; white-space: nowrap;
  }
  .contact-line svg { width: 16px; height: 16px; fill: none; stroke: var(--accent); stroke-width: 1.8; }
  .sep { color: var(--ink-soft); padding: 0 4px; }
</style>
</head>
<body>
<main class="canvas">
  <section class="card card--services">
    <div class="brand"><span class="brand-dot"></span>Bramblecrest Paving</div>
    <p class="services">
      asphalt construction and maintenance | drainage | foundations | retaining walls<br>
      chip seals | excavation | grading | landscape ground work | interlocking paver<br>
      hydro-seeding | structured and driveway demolition | utility trenching<br>
      and stump removal.
    </p>
  </section>

  <section class="card card--contact">
    <div class="brand"><span class="brand-dot"></span>Bramblecrest Paving</div>
    <p class="person-name">Gerald Pinsky</p>
    <p class="person-role">Operations Manager · lic#657920</p>
    <p class="address">418 Larkmoor St, Monterey, CA.</p>
    <p class="contact-line">
      <svg viewBox="0 0 16 16" aria-hidden="true"><path d="M4 1.5l2.5 3-1.5 1.8c.8 1.8 2.2 3.2 4 4l1.8-1.5 3 2.5-1.5 2.5C7 13.5 2.5 9 1.5 3z"/></svg>
      +999 9999 9999
      <span class="sep">|</span>
      <svg viewBox="0 0 16 16" aria-hidden="true"><rect x="1.5" y="3.5" width="13" height="9"/><path d="M1.5 3.5l6.5 5 6.5-5"/></svg>
      info@mywebsite.com
      <span class="sep">|</span>
      <svg viewBox="0 0 16 16" aria-hidden="true"><circle cx="8" cy="8" r="6.5"/><path d="M1.5 8h13M8 1.5c-3 3.5-3 9.5 0 13M8 1.5c3 3.5 3 9.5 0 13"/></svg>
      www.mywebsite.com
    </p>
  </section>
</main>
</body>
</html>
```